Business Cards

I'd like help creating business cards with the full logo "Veltrona Capital Partners" on the back of the card (navy background with white writing), and abbreviated logo "VCP" on the front. Would like to list name, title, phone number, email, and website listed on front of card. Would like to keep very simple. Front font Arial or similar.

```html
<!DOCTYPE html>
<html lang="en">
<head>
<meta charset="utf-8">
<title>Veltrona Capital Partners – Business Cards</title>
<link rel="stylesheet" href="https://fonts.googleapis.com/css2?family=Montserrat:wght@400;500;600;700&display=swap">
<style>
  :root {
    --backdrop: #252525;
    --navy: #203a6c;
    --navy-deep: #1c3362;
    --white: #ffffff;
    --emboss: #2b467a;
    --emboss-light: #6f86b6;
  }
  html, body {
    margin: 0;
    padding: 0;
    width: 1200px;
    height: 900px;
    overflow: hidden;
    background: var(--backdrop);
    font-family: "Montserrat", Arial, sans-serif;
  }
  .canvas {
    position: relative;
    width: 1200px;
    height: 900px;
  }
  .card {
    position: absolute;
    left: 300px;
    width: 600px;
    height: 343px;
    border-radius: 22px;
    background: linear-gradient(135deg, var(--navy) 0%, var(--navy-deep) 100%);
    box-shadow: 0 10px 24px rgba(0,0,0,0.45);
    overflow: hidden;
  }
  .card--back { top: 80px; }
  .card--front { top: 470px; }

  /* Back: full wordmark */
  .wordmark {
    position: absolute;
    left: 0; right: 0;
    top: 50%;
    transform: translateY(-50%);
    text-align: center;
    color: var(--emboss-light);
  }
  .wordmark__name {
    font-size: 58px;
    font-weight: 500;
    letter-spacing: 4px;
    line-height: 1;
  }
  .wordmark__sub {
    margin-top: 10px;
    font-size: 17px;
    font-weight: 500;
    letter-spacing: 11px;
  }

  /* Front */
  .identity {
    position: absolute;
    top: 44px;
    right: 44px;
    text-align: right;
    color: var(--white);
  }
  .identity__name {
    font-size: 22px;
    font-weight: 700;
    line-height: 1.1;
  }
  .identity__title {
    font-size: 13px;
    font-weight: 400;
    margin-top: 3px;
  }
  .monogram {
    position: absolute;
    left: 48px;
    top: 92px;
    display: flex;
    align-items: center;
    gap: 14px;
    color: var(--white);
  }
  .monogram__mark {
    width: 22px;
    height: 22px;
    background: var(--white);
  }
  .monogram__text {
    font-size: 64px;
    font-weight: 600;
    line-height: 1;
    letter-spacing: 2px;
  }
  .contact {
    position: absolute;
    left: 48px;
    bottom: 36px;
    color: var(--white);
    font-size: 14px;
    line-height: 1.35;
  }
  .contact__address { margin-bottom: 18px; }
  .contact__list {
    list-style: none;
    margin: 0;
    padding: 0;
  }
  .contact__item {
    display: flex;
    align-items: center;
    gap: 10px;
    margin-top: 4px;
  }
  .contact__icon {
    width: 14px;
    height: 14px;
    flex: none;
  }
  .faint-wordmark {
    position: absolute;
    right: 36px;
    bottom: 40px;
    text-align: center;
    color: var(--emboss);
  }
  .faint-wordmark__name {
    font-size: 36px;
    font-weight: 500;
    letter-spacing: 3px;
    line-height: 1;
  }
  .faint-wordmark__sub {
    margin-top: 6px;
    font-size: 11px;
    font-weight: 500;
    letter-spacing: 7px;
  }
</style>
</head>
<body>
<main class="canvas">

  <section class="card card--back" aria-label="Card back">
    <div class="wordmark">
      <div class="wordmark__name">VELTRONA</div>
      <div class="wordmark__sub">CAPITAL PARTNERS</div>
    </div>
  </section>

  <section class="card card--front" aria-label="Card front">
    <div class="identity">
      <div class="identity__name">Adrian Keller</div>
      <div class="identity__title">Managing Director</div>
    </div>

    <div class="monogram">
      <span class="monogram__mark"></span>
      <span class="monogram__text">VCP</span>
    </div>

    <div class="contact">
      <div class="contact__address">418 Harlow Park Ave, #112<br>Brookfield, OH 43190</div>
      <ul class="contact__list">
        <li class="contact__item">
          <svg class="contact__icon" viewBox="0 0 24 24" aria-hidden="true"><path fill="#ffffff" d="M6.6 10.8a15 15 0 0 0 6.6 6.6l2.2-2.2c.3-.3.7-.4 1-.2 1.1.4 2.3.6 3.6.6.6 0 1 .4 1 1V20c0 .6-.4 1-1 1A17 17 0 0 1 3 4c0-.6.4-1 1-1h3.5c.6 0 1 .4 1 1 0 1.3.2 2.5.6 3.6.1.3 0 .7-.2 1z"/></svg>
          <span>877-555-0196</span>
        </li>
        <li class="contact__item">
          <svg class="contact__icon" viewBox="0 0 24 24" aria-hidden="true"><rect x="2" y="5" width="20" height="14" rx="1" fill="#ffffff"/><path d="M2.5 6l9.5 7 9.5-7" fill="none" stroke="#203a6c" stroke-width="1.8"/></svg>
          <span>info@veltronacap.com</span>
        </li>
        <li class="contact__item">
          <svg class="contact__icon" viewBox="0 0 24 24" aria-hidden="true"><circle cx="12" cy="12" r="10" fill="#ffffff"/><path d="M2 12h20M12 2c3 3 3 17 0 20M12 2c-3 3-3 17 0 20" fill="none" stroke="#203a6c" stroke-width="1.4"/></svg>
          <span>www.veltronacap.com</span>
        </li>
      </ul>
    </div>

    <div class="faint-wordmark">
      <div class="faint-wordmark__name">VELTRONA</div>
      <div class="faint-wordmark__sub">CAPITAL PARTNERS</div>
    </div>
  </section>

</main>
</body>
</html>
```